Tamarind Crest Management - Business Cards

I need business cards. My current logo was designed by a designer at this site and I very much like and am happy with the results. I would like a business card that is trendy, unique, current yet professional. I deal with high net worth clients daily

Target Market(s)

Out of state investors looking to get into the rental market in Ohio

Industry/Entity Type

Property Management, Consulting

Contact Information for Business Card

Name, Title (Chief Financial Officer) office phone number (347) 681-9072 website address tamcrestmgmt.example

Font styles to use
Sans Serif

Colors
0054AA
0677BA
7BADD7
CADEEF
E8F1F8
0094D4
00A9DD
6FCCEA
C7EBF8
E9F6FB
00AB8E
00BBA5
67D7C9
C6EFE9
E9F9F6

```html
<!DOCTYPE html>
<html lang="en">
<head>
<meta charset="UTF-8">
<title>Tamarind Crest Management – Business Cards</title>
<link rel="stylesheet" href="https://fonts.googleapis.com/css2?family=Montserrat:wght@400;500;700;800&display=swap">
<style>
  :root {
    --navy: #22355e;
    --red: #d42030;
    --paper: #fafafa;
    --stage: #5e5e5e;
    --ink-soft: #2b3a5c;
  }
  * { box-sizing: border-box; margin: 0; padding: 0; }
  html, body {
    width: 1200px; height: 875px; overflow: hidden;
    background: var(--stage);
    font-family: "Montserrat", sans-serif;
  }
  .stage {
    width: 1200px; height: 875px;
    display: flex; flex-direction: column;
    align-items: center; justify-content: center; gap: 44px;
  }
  .card {
    position: relative;
    width: 620px; height: 354px;
    box-shadow: 0 10px 28px rgba(0,0,0,.35);
  }
  .card__frame {
    position: absolute; inset: 22px;
    border: 1.5px solid var(--red);
  }

  /* Back */
  .card--back { background: var(--navy); }
  .card--back .brand {
    position: absolute; inset: 0;
    display: flex; align-items: center; justify-content: center; gap: 14px;
  }
  .brand__mark {
    width: 22px; height: 22px; background: var(--red); flex: none;
  }
  .card--back .brand__name {
    color: #ffffff; font-weight: 800; font-size: 30px;
    letter-spacing: .5px; text-transform: uppercase;
    line-height: 1.1; text-align: left;
  }

  /* Front */
  .card--front { background: var(--paper); }
  .person {
    position: absolute; top: 52px; right: 52px; text-align: right;
  }
  .person__name {
    font-weight: 800; font-size: 24px; letter-spacing: .5px;
    text-transform: uppercase; color: var(--navy);
  }
  .person__first { color: var(--red); }
  .person__title {
    font-weight: 500; font-size: 13px; color: var(--ink-soft); margin-top: 2px;
  }
  .wordmark {
    position: absolute; left: 56px; top: 118px;
    color: var(--navy); font-weight: 800; font-size: 26px;
    text-transform: uppercase; line-height: 1.15; letter-spacing: .5px;
  }
  .contacts {
    position: absolute; left: 56px; bottom: 52px;
    list-style: none; display: flex; flex-direction: column; gap: 8px;
  }
  .contacts li {
    display: flex; align-items: center; gap: 10px;
    font-size: 14px; font-weight: 500; color: var(--navy);
  }
  .contacts svg { width: 14px; height: 14px; flex: none; }
</style>
</head>
<body>
<main class="stage">
  <section class="card card--back" aria-label="Card back">
    <div class="card__frame"></div>
    <div class="brand">
      <span class="brand__mark"></span>
      <span class="brand__name">Tamarind Crest<br>Management</span>
    </div>
  </section>

  <section class="card card--front" aria-label="Card front">
    <div class="card__frame"></div>
    <div class="person">
      <p class="person__name"><span class="person__first">Dana</span> Whitfield</p>
      <p class="person__title">Chief Financial Officer</p>
    </div>
    <p class="wordmark">Tamarind Crest<br>Management</p>
    <ul class="contacts">
      <li>
        <svg viewBox="0 0 16 16" aria-hidden="true"><path fill="#d42030" d="M3.6 1.5l2.3 2.6-1.3 1.9c.9 2 2.4 3.5 4.4 4.4l1.9-1.3 2.6 2.3-1.6 2.6C6.9 13.7 2.3 9.1 1 4.1z"/></svg>
        +1 (347) 681-9072
      </li>
      <li>
        <svg viewBox="0 0 16 16" aria-hidden="true"><rect x="1" y="3" width="14" height="10" rx="1" fill="#d42030"/><path d="M1.8 4l6.2 5 6.2-5" stroke="#fff" stroke-width="1.4" fill="none"/></svg>
        info@tamcrestmgmt.example
      </li>
      <li>
        <svg viewBox="0 0 16 16" aria-hidden="true"><circle cx="8" cy="8" r="6.5" fill="#d42030"/><path d="M1.5 8h13M8 1.5c-3 3.5-3 9.5 0 13M8 1.5c3 3.5 3 9.5 0 13" stroke="#fff" stroke-width="1" fill="none"/></svg>
        www.tamcrestmgmt.example
      </li>
    </ul>
  </section>
</main>
</body>
</html>
```